Prescription Savings Card

Looking to revamp our cards that are distributed to pharmacies. Processing information must stand out and be in black with lines through zeros for easy identification.
I have included some previous card designs for consideration. we are looking to go with something cleaner with mainly processing information on the back similar to all white version attached.
Target Market(s)
Pharmacists and Pharmacy Technicians
Industry/Entity Type
prescription medications
Contact Information for Business Card
processing information
Requirements
Must have
- easy to read processing information

```html
<!DOCTYPE html>
<html lang="en">
<head>
<meta charset="utf-8">
<title>MedSave Prescription Drug Card</title>
<link rel="stylesheet" href="https://fonts.googleapis.com/css2?family=Roboto:wght@400;500;700;900&display=swap">
<style>
  :root {
    --stage: #111111;
    --navy: #3a4c7e;
    --red: #df3237;
    --white: #ffffff;
    --ink: #111111;
    --grey: #7d7d7d;
    --light-grey: #b8b8b8;
  }
  * { box-sizing: border-box; margin: 0; padding: 0; }
  html, body { width: 1200px; height: 1000px; overflow: hidden; background: var(--stage); }
  body { position: relative; font-family: "Roboto", Arial, sans-serif; }

  .card {
    position: absolute;
    left: 294px;
    width: 613px;
    height: 352px;
    border-radius: 22px;
    overflow: hidden;
  }
  .card-shapes { position: absolute; inset: 0; width: 100%; height: 100%; }

  /* Front */
  .card-front { top: 149px; background: var(--white); }
  .brand-front {
    position: absolute; left: 39px; top: 43px;
    font-size: 26px; font-weight: 900; letter-spacing: -0.8px;
    color: var(--navy);
  }
  .eyebrow {
    position: absolute; left: 35px; top: 127px;
    font-size: 16px; font-weight: 400; letter-spacing: 3.6px;
    color: var(--red);
  }
  .card-title {
    position: absolute; left: 33px; top: 152px;
    font-size: 46px; font-weight: 400; line-height: 53px;
    color: var(--navy);
  }
  .pricing-note {
    position: absolute; left: 37px; top: 275px;
    font-size: 13px; color: var(--grey);
  }
  .web-address {
    position: absolute; left: 37px; top: 318px;
    font-size: 13px; font-weight: 700; color: var(--navy);
  }
  .web-address .tld { font-weight: 400; color: var(--light-grey); }

  /* Back */
  .card-back { top: 570px; background: var(--red); color: var(--white); }
  .brand-back {
    position: absolute; left: 26px; top: 27px;
    font-size: 38px; font-weight: 900; letter-spacing: -1.4px;
    color: var(--white);
  }
  .benefits {
    position: absolute; left: 101px; top: 140px;
    list-style: none; font-size: 19.5px; line-height: 24.5px;
  }
  .benefits li { padding-left: 12px; text-indent: -12px; }
  .benefits li::before { content: "•"; font-size: 14px; margin-right: 6px; vertical-align: 2px; }
  .processing {
    position: absolute; left: 360px; top: 137px; width: 184px;
    font-size: 24px; font-weight: 700; line-height: 31px;
    color: var(--ink);
  }
  .processing .row { display: flex; justify-content: space-between; }
  .processing dd { font-weight: 700; }
  .zero { position: relative; display: inline-block; }
  .zero::after {
    content: "";
    position: absolute;
    left: 50%; top: 22%;
    width: 2.5px; height: 58%;
    background: currentColor;
    transform: translateX(-50%) rotate(30deg);
  }
  .help-line {
    position: absolute; left: 108px; top: 299px;
    font-size: 14px; line-height: 18px;
  }
  .help-line strong { font-weight: 700; }
</style>
</head>
<body>

<section class="card card-front" aria-label="Card front">
  <svg class="card-shapes" viewBox="0 0 613 352" preserveAspectRatio="none" aria-hidden="true">
    <polygon points="94,0 613,0 613,258" fill="var(--navy)"/>
    <polygon points="613,258 613,352 425,352" fill="var(--red)"/>
  </svg>
  <div class="brand-front">MedSave</div>
  <p class="eyebrow">DISCOUNTING</p>
  <h1 class="card-title">Prescription<br>Drug Card</h1>
  <p class="pricing-note">Check Current Pricing on our Website</p>
  <p class="web-address">MedSave<span class="tld">.com</span></p>
</section>

<section class="card card-back" aria-label="Card back">
  <svg class="card-shapes" viewBox="0 0 613 352" preserveAspectRatio="none" aria-hidden="true">
    <polygon points="0,0 351,0 0,152" fill="var(--navy)"/>
  </svg>
  <div class="brand-back">MedSave</div>
  <ul class="benefits">
    <li>Save up to 99%</li>
    <li>100% HIPAA Compliant</li>
    <li>Lower Price Guarantee</li>
    <li>Covers 90 Days Supply<br>&amp; Pet Meds</li>
  </ul>
  <dl class="processing">
    <div class="row"><dt>BIN:</dt><dd><span class="zero">0</span><span class="zero">0</span><span class="zero">0</span><span class="zero">0</span><span class="zero">0</span><span class="zero">0</span></dd></div>
    <div class="row"><dt>ID:</dt><dd>RX<span class="zero">0</span><span class="zero">0</span><span class="zero">0</span><span class="zero">0</span></dd></div>
    <div class="row"><dt>PCN:</dt><dd>RX<span class="zero">0</span><span class="zero">0</span><span class="zero">0</span></dd></div>
    <div class="row"><dt>GROUP:</dt><dd>RX<span class="zero">0</span><span class="zero">0</span><span class="zero">0</span><span class="zero">0</span></dd></div>
  </dl>
  <p class="help-line">If you are unable to process a prescription through our program<br>please call <strong>(800)-555-0143</strong></p>
</section>

</body>
</html>
```